Mortgage Broking boutique Business

I’m wanting a revamped look to my existing business card design. I do like the black and silver but happy to have other colours introduced based on your creation. I’ve attached a copy of my current card so you can have a starting point updated details noted brloe. I deal with high net worth individuals so need my card to be sophisticated, classy that gives off a classy vibe

Target Market(s)

High net worth, wealthy

Industry/Entity Type

Mortgage Brokerage

Contact Information for Business Card

Job title: Finance Executive
Phone: +61 7 3287 4419
Mobile: 0471 352 608
Email: marcus@quillbrookcapital.com.au
Web: www.quillbrookcapital.com.au
Address: level 36 Tindale Court, 58 Harwick St Brisbane QLD 4000

Font styles to use
Other font styles liked:
• Helvetica

Colors

Designer to choose colors to be used in the design.

Requirements
Must have
• Use my existing card design as a starting point

```html
<!DOCTYPE html>
<html lang="en">
<head>
<meta charset="utf-8">
<title>Quillbrook Capital – Business Card</title>
<link rel="stylesheet" href="https://fonts.googleapis.com/css2?family=Jost:wght@300;400;500&family=Open+Sans:wght@300;700&display=swap">
<style>
  :root{
    --stage:#1c1f24;
    --card:#2b2b2d;
    --card-edge:#1e1e20;
    --silver:#e9e9ea;
    --silver-mid:#b9b9bc;
    --silver-dim:#8d8d91;
    --name:#a9a9ad;
  }
  *{margin:0;padding:0;box-sizing:border-box}
  html,body{width:1200px;height:900px;overflow:hidden;background:var(--stage)}
  .canvas{position:relative;width:1200px;height:900px;display:flex;flex-direction:column;align-items:center;justify-content:center;gap:40px}
  .card{position:relative;width:700px;height:400px;border-radius:34px;background:linear-gradient(160deg,#323234 0%,var(--card) 55%,#252527 100%);box-shadow:0 0 0 1px var(--card-edge),0 18px 40px rgba(0,0,0,.45);overflow:hidden}

  /* front */
  .front .rule{position:absolute;height:2px}
  .front .rule-left{left:0;top:128px;width:150px;background:linear-gradient(90deg,transparent,var(--silver))}
  .front .rule-right{right:0;top:272px;width:150px;background:linear-gradient(90deg,var(--silver),transparent)}
  .front .wordmark{position:absolute;left:160px;top:100px;width:380px;text-align:center;font-family:"Jost",sans-serif;color:var(--silver)}
  .wordmark .primary{display:block;font-weight:400;font-size:56px;letter-spacing:12px;line-height:1}
  .wordmark .secondary{display:block;font-weight:400;font-size:24px;letter-spacing:9px;margin-top:8px}
  .front .underline{position:absolute;left:190px;top:228px;width:310px;height:1px;background:linear-gradient(90deg,transparent,var(--silver-mid),transparent)}
  .front .web{position:absolute;left:0;right:0;top:300px;text-align:center;font-family:"Jost",sans-serif;font-size:20px;color:var(--silver);letter-spacing:.5px}

  /* back */
  .back .person{position:absolute;left:58px;top:40px;font-family:"Open Sans",sans-serif}
  .person .name{font-weight:700;font-size:21px;color:var(--name)}
  .person .title{font-weight:300;font-size:14px;color:var(--silver-dim);padding-bottom:4px;border-bottom:1px solid var(--silver-dim);display:inline-block}
  .back .wordmark{position:absolute;left:58px;top:150px;font-family:"Jost",sans-serif;color:var(--silver);text-align:center;width:270px}
  .back .wordmark .primary{font-size:38px;letter-spacing:8px}
  .back .wordmark .secondary{font-size:17px;letter-spacing:7px;margin-top:4px}
  .back .divider{position:absolute;left:350px;top:150px;width:2px;height:200px;background:linear-gradient(180deg,var(--silver),rgba(233,233,234,.1))}
  .contacts{position:absolute;left:372px;top:148px;list-style:none;font-family:"Jost",sans-serif;font-size:18px;color:var(--silver-mid);line-height:1.2}
  .contacts li{display:flex;align-items:flex-start;gap:10px;margin-bottom:5px}
  .contacts .icon{flex:0 0 18px;width:18px;height:18px;margin-top:2px}
  .contacts .indent{padding-left:28px}
</style>
</head>
<body>
<main class="canvas">

  <section class="card front" aria-label="Card front">
    <div class="rule rule-left"></div>
    <div class="rule rule-right"></div>
    <div class="wordmark">
      <span class="primary">QUILLBROOK</span>
      <span class="secondary">CAPITAL</span>
    </div>
    <div class="underline"></div>
    <p class="web">www.quillbrookcapital.com.au</p>
  </section>

  <section class="card back" aria-label="Card back">
    <div class="person">
      <p class="name">Example Name</p>
      <p class="title">Finance Executive</p>
    </div>
    <div class="wordmark">
      <span class="primary">QUILLBROOK</span>
      <span class="secondary">CAPITAL</span>
    </div>
    <div class="divider"></div>
    <ul class="contacts">
      <li>
        <svg class="icon" viewBox="0 0 18 18"><rect width="18" height="18" rx="3" fill="#c9c9cc"/><path d="M9 3.5a3.5 3.5 0 0 0-3.5 3.5c0 2.6 3.5 7 3.5 7s3.5-4.4 3.5-7A3.5 3.5 0 0 0 9 3.5zm0 4.8a1.3 1.3 0 1 1 0-2.6 1.3 1.3 0 0 1 0 2.6z" fill="#2b2b2d"/></svg>
        <span>level 36 Tindale Court,</span>
      </li>
      <li class="indent">58 Harwick St Brisbane QLD 4000</li>
      <li>
        <svg class="icon" viewBox="0 0 18 18"><rect width="18" height="18" rx="3" fill="#c9c9cc"/><path d="M5.5 4h2l1 2.5-1.3 1a6 6 0 0 0 3.3 3.3l1-1.3 2.5 1v2a1 1 0 0 1-1 1A9 9 0 0 1 4.5 5a1 1 0 0 1 1-1z" fill="#2b2b2d"/></svg>
        <span>+61 7 3287 4419</span>
      </li>
      <li>
        <svg class="icon" viewBox="0 0 18 18"><rect width="18" height="18" rx="3" fill="#c9c9cc"/><rect x="6" y="3" width="6" height="12" rx="1" fill="#2b2b2d"/><rect x="7" y="4.5" width="4" height="7.5" fill="#c9c9cc"/></svg>
        <span>0471 352 608</span>
      </li>
      <li>
        <svg class="icon" viewBox="0 0 18 18"><rect width="18" height="18" rx="3" fill="#c9c9cc"/><rect x="3.5" y="5" width="11" height="8" rx="1" fill="#2b2b2d"/><path d="M4 5.5l5 4 5-4" stroke="#c9c9cc" stroke-width="1" fill="none"/></svg>
        <span>marcus@quillbrookcapital.com.au</span>
      </li>
      <li>
        <svg class="icon" viewBox="0 0 18 18"><rect width="18" height="18" rx="3" fill="#c9c9cc"/><circle cx="9" cy="9" r="5" fill="none" stroke="#2b2b2d" stroke-width="1.2"/><path d="M4 9h10M9 4c-2.5 3-2.5 7 0 10M9 4c2.5 3 2.5 7 0 10" fill="none" stroke="#2b2b2d" stroke-width="1"/></svg>
        <span>www.quillbrookcapital.com.au</span>
      </li>
    </ul>
  </section>

</main>
</body>
</html>
```